Brent Oakes Director / Photographer Branding

I need note pads, envelops, business cards and letter head for my company. I'm a fashion and advertising director / photographer. I'm having trouble deciding how to include both Director & Photographer in my title or if it is even necessary. Maybe just my name is enough. I'm open for even using my initials if it works with the design and overall pieces. Please view my website to see what I have at this moment and what work I do. www.brentoakesstudio-mail.net
Updates

Project Deadline Extended
Reason: Hello Everyone! I'm extending the deadline since I have been traveling on a job out of country and I wanted to have more time to look through all the designs and give enough time for everyone to provide changes with designs and updates. I will be more available to communicate online now that I'm back in the office! Thank you! Brent Oakes

Target Market(s)

Fashion magazines, clothing lines and beauty cosmetic brands.

Industry/Entity Type

Fashion Photography

Font styles to use
Sans Serif

Colors
acd036
acd35d
cbcbcb
f5f5f5

Requirements
Must have
• My name.. Brent Oakes, my website: brentoakesstudio-mail.net my phone number, 555-284-6103
• I don't need my address on these. I also live by the philosophy that less is more and keeping things simple ads strength to a design. I also don't want to stop people from taking chances and experimenting with an idea that might take me down different road with my branding.
Nice to have
• Bold designs and clean lines. I'm open to ideas that I could adopt but I lean towards a more minimalistic look in general.
Should not have
• Not have cheesy graphics or pictures. No images of cameras, film or anything that looks like it is a camera or aperture, lens etc... ;)

```html
<!DOCTYPE html>
<html lang="en">
<head>
<meta charset="utf-8">
<title>Brent Oakes Letterhead</title>
<link href="https://fonts.googleapis.com/css2?family=Arimo:wght@400&family=Raleway:wght@200;400&display=swap" rel="stylesheet">
<style>
  :root {
    --lime: #acd036;
    --lime-soft: #acd35d;
    --grey: #cbcbcb;
    --grey-dark: #9a9a9a;
    --paper: #ffffff;
    --backdrop: #f5f5f5;
    --ink: #2b2b2b;
    --muted: #8c8c8c;
  }
  * { box-sizing: border-box; margin: 0; padding: 0; }
  html, body { width: 1200px; height: 784px; overflow: hidden; background: var(--backdrop); }
  .letterhead {
    position: absolute; left: 340px; top: 24px;
    width: 520px; height: 736px;
    background: var(--paper);
    box-shadow: 0 2px 10px rgba(0,0,0,0.08);
    font-family: "Arimo", Arial, sans-serif;
    color: var(--ink);
  }
  .top-rule {
    position: absolute; left: 40px; top: 22px; width: 340px; height: 3px;
    background: var(--lime);
  }
  .masthead {
    position: absolute; left: 388px; top: 15px; white-space: nowrap;
  }
  .masthead-name {
    font-family: "Raleway", sans-serif; font-weight: 400;
    font-size: 11px; line-height: 13px; letter-spacing: 1.5px; color: var(--lime);
  }
  .masthead-title {
    font-size: 6.5px; color: var(--muted); margin-top: 2px;
  }
  .top-rule-end {
    position: absolute; left: 478px; top: 44px; width: 42px; height: 6px;
    background: var(--grey-dark);
  }
  .name-column {
    position: absolute; left: 40px; top: 58px; width: 36px;
    display: flex; flex-direction: column; align-items: center; gap: 24px;
    font-family: "Raleway", sans-serif; font-weight: 200;
    font-size: 30px; line-height: 34px; color: var(--lime);
  }
  .letter-body {
    position: absolute; left: 130px; top: 70px; width: 340px;
    font-size: 9.5px; line-height: 13px;
  }
  .letter-body p { margin-bottom: 13px; }
  .signature {
    position: absolute; left: 300px; top: 470px; width: 130px; height: 42px;
    background: #f6f6f6;
  }
  .footer-band {
    position: absolute; left: 0; bottom: 0; width: 100%; height: 8px;
    display: flex;
  }
  .footer-band .band-grey { width: 60px; background: var(--grey-dark); }
  .footer-band .band-lime { flex: 1; background: var(--lime); }
  .contacts {
    position: absolute; left: 40px; bottom: 34px; width: 440px;
    display: flex; justify-content: space-between; align-items: flex-end;
  }
  .contact { display: flex; flex-direction: column; align-items: center; gap: 6px; }
  .contact svg { width: 12px; height: 12px; }
  .contact span { font-size: 8px; color: var(--muted); white-space: nowrap; }
</style>
</head>
<body>
  <article class="letterhead">
    <div class="top-rule"></div>
    <div class="masthead">
      <div class="masthead-name">BRENT OAKES</div>
      <div class="masthead-title">Director / Photographer</div>
    </div>
    <div class="top-rule-end"></div>

    <div class="name-column" aria-label="Brent Oakes">
      <span>B</span><span>R</span><span>E</span><span>N</span><span>T</span>
      <span>O</span><span>A</span><span>K</span><span>E</span><span>S</span>
    </div>

    <section class="letter-body">
      <p>Lorem Ipsum is simply dummy text of the printing and typesetting industry. Lorem Ipsum has been the industry's standard dummy text ever since the 1500s, when an unknown printer took a galley of type and scrambled it to make a type specimen book. It has survived not only five centuries, but also the leap into electronic typesetting, remaining essentially unchanged. It was popularised in the 1960s with the release of Letrafix sheets containing Lorem Ipsum passages, and more recently with desktop publishing software like Folio Layout including versions of Lorem Ipsum.</p>
      <p>It is a long established fact that a reader will be distracted by the readable content of a page when looking at its layout. The point of using Lorem Ipsum is that it has a more-or-less normal distribution of letters, as opposed to using 'Content here, content here', making it look like readable English. Many desktop publishing packages and web page editors now use Lorem Ipsum as their default model text, and a search for 'lorem ipsum' will uncover many web sites still in their infancy. Various versions have evolved over the years, sometimes by accident, sometimes on purpose (injected humour and the like).</p>
      <p>Contrary to popular belief, Lorem Ipsum is not simply random text. It has roots in a piece of classical Latin literature from 45 BC, making it over 2000 years old. Richard Pellmore, a Latin professor at Westbrook College in Vermont, looked up one of the more obscure Latin words, consectetur, from a Lorem Ipsum passage, and going through the cites of the word in classical literature, discovered the undoubtable source. Lorem Ipsum comes from sections 1.10.32 and 1.10.33 of "de Finibus Bonorum et Malorum" structures, to generate Lorem Ipsum which looks reasonable. The generated Lorem Ipsum is therefore always free from repetition, injected humour, or non-characteristic words etc.</p>
    </section>

    <div class="signature" role="img" aria-label="Handwritten signature"></div>

    <footer class="contacts">
      <div class="contact">
        <svg viewBox="0 0 12 12" aria-hidden="true"><rect x="0.5" y="2" width="11" height="8" fill="var(--lime)"/><path d="M0.5 2 L6 6.5 L11.5 2" fill="none" stroke="#fff" stroke-width="1"/></svg>
        <span>brent@brentoakesstudio-mail.net</span>
      </div>
      <div class="contact">
        <svg viewBox="0 0 12 12" aria-hidden="true"><path d="M2.5 1 L4.5 1 L5.3 3.6 L4 4.6 C4.8 6.4 5.8 7.4 7.4 8 L8.4 6.7 L11 7.5 L11 9.5 C11 10.4 10.3 11 9.4 11 C4.8 10.6 1.4 7.2 1 2.6 C1 1.7 1.6 1 2.5 1 Z" fill="var(--lime)"/></svg>
        <span>555-284-6103</span>
      </div>
      <div class="contact">
        <svg viewBox="0 0 12 12" aria-hidden="true"><circle cx="6" cy="6" r="5.5" fill="var(--lime)"/><path d="M0.5 6 H11.5 M6 0.5 C3.5 3 3.5 9 6 11.5 M6 0.5 C8.5 3 8.5 9 6 11.5" fill="none" stroke="#fff" stroke-width="0.7"/></svg>
        <span>www.brentoakesstudio-mail.net</span>
      </div>
      <div class="contact">
        <svg viewBox="0 0 12 12" aria-hidden="true"><rect x="1" y="1" width="10" height="10" fill="var(--lime)"/></svg>
        <span>@brentoakes</span>
      </div>
    </footer>

    <div class="footer-band">
      <div class="band-grey"></div>
      <div class="band-lime"></div>
    </div>
  </article>
</body>
</html>
```